Byteway Tech Services Flyer

I have a retail Computer Store that I want to promote in the local area.
The target market is seniors aged between 40-80 year olds. I need to create a flyer for the business to do a flyer drop to homes and business advertising the business & services we offer. I would also like to drop this on our socials for online target ads.
Store Name: Byteway Tech systems Address: 17 Larkspur Road, DONVALE Victoria 3111 Phone Number: (03) 9521 6408 Target Audience: older generation between 40 - 90 year olds Services offered: Retail Sales & Service, Complete Workshop Facilities, Cloud services, Deskly 240 Experts, Network & Wireless Products, Managed Services, PC & Laptop Sales, Custom Built Computers Vendors: Veltrix, QORNL, Parvanix Partner, Olex, Brimo, KT & Rune Reseller Please keep it to A1 size and double sided with options to go A3 o A4 later.

Target Market(s)

Residential home users

Industry/Entity Type

www.bytewaytech.com.au

Font styles to use
Sans Serif

Colors
0054AA
0677BA
7BADD7
CADEEF
E8F1F8

Requirements
Must have
• Simple target is the elderly population

```html
<!DOCTYPE html>
<html lang="en">
<head>
<meta charset="utf-8">
<title>Byteway Tech Services Flyer</title>
<link href="https://fonts.googleapis.com/css2?family=Poppins:wght@400;500;600;700;800&display=swap" rel="stylesheet">
<style>
  :root {
    --navy: #0b2f5c;
    --navy-deep: #082546;
    --brand-blue: #0054AA;
    --mid-blue: #0677BA;
    --sky: #7BADD7;
    --pale: #CADEEF;
    --mist: #E8F1F8;
    --ink: #111a2b;
    --white: #ffffff;
    --backdrop: #dcdcdc;
  }
  * { margin: 0; padding: 0; box-sizing: border-box; }
  html, body { width: 1200px; height: 2182px; overflow: hidden; }
  body { background: var(--backdrop); font-family: "Poppins", sans-serif; position: relative; }

  .flyer {
    position: absolute; left: 50px; top: 314px;
    width: 927px; height: 1310px;
    transform: scale(1.1866); transform-origin: top left;
    background: var(--white);
    box-shadow: 0 4px 14px rgba(0,0,0,.25);
    overflow: hidden;
  }
  .flyer-shapes { position: absolute; inset: 0; }

  .brand { position: absolute; right: 32px; top: 40px; display: flex; align-items: center; gap: 12px; }
  .brand-mark { width: 46px; height: 46px; background: var(--brand-blue); }
  .brand-name { font-size: 30px; font-weight: 600; color: var(--brand-blue); letter-spacing: 4px; line-height: 1; }

  .headline { position: absolute; left: 48px; top: 125px; color: var(--white); font-weight: 800; font-size: 72px; line-height: 76px; letter-spacing: 1px; }
  .tagline { position: absolute; left: 48px; top: 298px; color: var(--pale); font-weight: 600; font-size: 20.5px; }
  .intro { position: absolute; left: 48px; top: 344px; width: 832px; color: var(--white); font-size: 17px; line-height: 22px; text-align: justify; }

  .vendors-frame { position: absolute; left: 30px; top: 676px; width: 280px; height: 354px; background: rgba(232,241,248,.75); }
  .vendors { position: absolute; left: 44px; top: 694px; width: 252px; height: 336px; background: var(--brand-blue); color: var(--white); padding: 20px 16px; }
  .vendors h2 { font-size: 23px; font-weight: 700; line-height: 30px; }
  .vendors ul { list-style: none; margin-top: 6px; padding-left: 34px; }
  .vendors li { font-size: 18px; font-weight: 600; line-height: 32.6px; }
  .vendors li::before, .services li::before { content: "• "; }

  .services { position: absolute; left: 426px; top: 960px; }
  .services h2 { color: var(--brand-blue); font-size: 24px; font-weight: 700; }
  .services ul { list-style: none; margin-top: 8px; padding-left: 34px; }
  .services li { color: var(--ink); font-size: 18.5px; font-weight: 600; line-height: 37.5px; }

  .store-info { position: absolute; left: 53px; top: 1082px; color: var(--brand-blue); }
  .store-info .label { font-size: 14px; font-weight: 500; }
  .store-info .hours { font-size: 18px; font-weight: 700; color: var(--navy); margin-bottom: 16px; }
  .store-info .address { font-size: 18px; line-height: 22px; margin-bottom: 20px; }
  .store-info .help { font-size: 16px; }
  .store-info .phone { font-size: 27px; font-weight: 700; color: var(--navy); margin-top: 6px; }
</style>
</head>
<body>
<main class="flyer">
  <svg class="flyer-shapes" viewBox="0 0 927 1310" width="927" height="1310">
    <defs>
      <linearGradient id="heroTone" x1="0" y1="0" x2="1" y2="1">
        <stop offset="0" stop-color="#0c3466"/>
        <stop offset="1" stop-color="#082546"/>
      </linearGradient>
      <linearGradient id="bandTone" x1="0" y1="0" x2="1" y2="0">
        <stop offset="0" stop-color="#5a6470"/>
        <stop offset="0.5" stop-color="#3d4a5a"/>
        <stop offset="1" stop-color="#8f9aa3"/>
      </linearGradient>
    </defs>
    <polygon points="0,0 927,262 927,552 0,552" fill="url(#heroTone)" role="img" aria-label="Dark blue tinted close-up of a circuit board"/>
    <rect x="0" y="552" width="927" height="195" fill="url(#bandTone)" role="img" aria-label="Close-up photo of a computer motherboard with expansion slots"/>
    <rect x="310" y="764" width="200" height="168" fill="#4a6a8c" role="img" aria-label="Photo of a technician screwing a component into a computer case"/>
    <rect x="518" y="764" width="200" height="168" fill="#3e5670" role="img" aria-label="Photo of hands installing memory into a desktop computer"/>
    <rect x="726" y="764" width="201" height="168" fill="#1f4d86" role="img" aria-label="Photo of a technician working inside a computer tower"/>
    <polygon points="0,1288 470,1288 450,1310 0,1310" fill="var(--brand-blue)"/>
    <polygon points="478,1288 927,1288 927,1310 458,1310" fill="var(--sky)"/>
  </svg>

  <div class="brand">
    <span class="brand-mark"></span>
    <span class="brand-name">BYTEWAY TECH</span>
  </div>

  <h1 class="headline">NEW<br>COMPUTER</h1>
  <p class="tagline">DON’T KNOW WHERE TO START….? DON’T KNOW WHAT YOU NEED….?</p>
  <p class="intro">Want to keep up with the latest in technology? We can help you. Whether you are a small or medium business, run a home office, or are a passionate “Gamer”, we can come up with the perfect solution to your computer needs.</p>

  <div class="vendors-frame"></div>
  <section class="vendors">
    <h2>CUSTOM BUILT<br>COMPUTERS<br>VENDORS:</h2>
    <ul>
      <li>Veltrix</li>
      <li>QORNL</li>
      <li>Parvanix Partner</li>
      <li>Olex</li>
      <li>Brimo</li>
      <li>KT &amp; Rune Reseller</li>
    </ul>
  </section>

  <section class="services">
    <h2>SERVICES OFFERED:</h2>
    <ul>
      <li>Retail Sales &amp; Service</li>
      <li>Complete Workshop Facilities</li>
      <li>Cloud services</li>
      <li>Deskly 240 Experts</li>
      <li>Network &amp; Wireless Products</li>
      <li>Managed Services</li>
      <li>PC &amp; Laptop Sales</li>
    </ul>
  </section>

  <section class="store-info">
    <p class="label">STORE MON - FRI</p>
    <p class="hours">9:00 AM - 5:30 PM</p>
    <p class="address">17 Larkspur Road,<br>KELLSWOOD Northvale 4820</p>
    <p class="help">Need Help? Phone Number:</p>
    <p class="phone">(03) 9521 6408</p>
  </section>
</main>
</body>
</html>
```